Web Banners

I need banners to run ads in Chatterly and plume ads. No flash needed. Just static or animated as you see fit.

Our website: www.tidewavecourses.com
The banners will be promoting our surf camps in Kelso and Marrowby as "Harbor Retreats".

I will be using this 3rd party site to list my ads. Here are their full requirements:
http://support.bannerlift.com/creative-requirements/

These are the banners I need
- Banner – 468×60
- Square – 250×250
- Small Square – 200×200
- Leaderboard – 728×90
- Medium Rectangle – 300×250
- Large Rectangle – 336×280
- Skyscraper – 120×600
- Wide Skyscraper – 160×600
- Mobile Leaderboard – 320×50
- Chatterly – 100×72
- Chatterly News Feed – 200×200, 600×315

For proofing purposes, if you want to do 1 or 2 in the beginning, that's fine.
Once we approve your direction, I would need the remaining banners before final payment is made. I have included some graphics to get you started.

Key focus for any statements would be:
learn from pro surfers
make new friends
learn how to surf
improve your surfing skills

```html
<!DOCTYPE html>
<html lang="en">
<head>
<meta charset="utf-8">
<title>Harbor Retreats – Leaderboard Banner</title>
<link href="https://fonts.googleapis.com/css2?family=Bangers&display=swap" rel="stylesheet">
<style>
  :root {
    --teal-light: #5fe0c4;
    --teal: #2fc0b0;
    --teal-deep: #1a9a94;
    --navy: #12263a;
    --headline: #f4e62c;
    --headline-edge: #1b2a2a;
    --sky: #bfe3f2;
    --sea: #2ba7c4;
    --sand: #e9dcc0;
  }
  html, body {
    margin: 0;
    padding: 0;
    overflow: hidden;
    background: #ffffff;
  }
  .banner {
    position: relative;
    width: 1200px;
    height: 148px;
    overflow: hidden;
    font-family: 'Bangers', 'Impact', sans-serif;
  }
  .texture-panel {
    position: absolute;
    left: 0; top: 0;
    width: 500px; height: 148px;
    background: linear-gradient(100deg, var(--teal-deep) 0%, var(--teal-light) 35%, var(--teal) 65%, var(--teal-light) 100%);
  }
  .photo {
    position: absolute;
    top: 0;
    height: 148px;
  }
  .photo--beginners {
    left: 500px;
    width: 395px;
    background: linear-gradient(180deg, var(--sky) 0%, var(--sky) 30%, var(--sea) 55%, #7fd0dc 80%, var(--sand) 100%);
  }
  .photo--standing {
    left: 895px;
    width: 305px;
    background: linear-gradient(180deg, #cfe8ef 0%, #9fd3e0 35%, var(--sea) 65%, #5dbfcf 100%);
    border-left: 3px solid #ffffff;
  }
  .brand {
    position: absolute;
    left: 34px;
    top: 34px;
    display: flex;
    align-items: center;
    gap: 14px;
  }
  .brand__name {
    color: var(--navy);
    font-size: 34px;
    line-height: 0.95;
    letter-spacing: 1px;
    text-transform: uppercase;
    margin: 0;
  }
  .brand__mark {
    width: 58px;
    height: 58px;
    border-radius: 50%;
    background: var(--navy);
  }
  .headline {
    position: absolute;
    left: 322px;
    top: 54px;
    margin: 0;
    color: var(--headline);
    font-size: 38px;
    font-weight: 400;
    letter-spacing: 1.5px;
    white-space: nowrap;
    text-shadow:
      2px 2px 0 var(--headline-edge),
      -1px -1px 0 var(--headline-edge),
      1px -1px 0 var(--headline-edge),
      -1px 1px 0 var(--headline-edge);
  }
</style>
</head>
<body>
  <div class="banner">
    <div class="texture-panel" role="img" aria-label="Turquoise painted texture background"></div>
    <div class="photo photo--beginners" role="img" aria-label="Photo of young surfers learning on foam boards in shallow waves"></div>
    <div class="photo photo--standing" role="img" aria-label="Photo of a young surfer standing up on a board in the whitewater"></div>

    <div class="brand">
      <p class="brand__name">Harbor<br>Retreats</p>
      <span class="brand__mark" aria-hidden="true"></span>
    </div>

    <h1 class="headline">+Improve Your Surfing Skillsers</h1>
  </div>
</body>
</html>
```